Storage Company Newsletter

We need a design for a newsletter for our company Vaultrix, a digital and physical asset storage company .The newsletter will be informative and educational covering tips on secure storage of personal documents and items both at home and at the work place. Rest easy with Vaultrix is our mantra. We have a pre-existing trademark & logo. Colors are blue and green. We can share the cmyk/rgb color information and background is grey.

Target Market(s)

Mass market – Middle to High income individuals

Industry/Entity Type

Digital

Font styles to use
Sans Serif

Colors
0393ce
00a88f
edf2f7

Requirements
Must have
• The newsletter linked to a CMS. In HTML5; Mail-chimp integration readable on Gmail, Yahoo, Hotmail and Outlook
Nice to have
• Sections of the newsletter are:
• Cover story
• News Flash
• Mwanachi Perspective
• Spotlight on the Counties
• CEO's Corner
• Tips and Helpful Information
• Important Dates and Events

```html
<!DOCTYPE html>
<html lang="en">
<head>
<meta charset="utf-8">
<title>Vaultrix Newsletter</title>
<link rel="stylesheet" href="https://fonts.googleapis.com/css2?family=Exo+2:wght@600;700;800&family=Source+Sans+3:wght@400;600&display=swap">
<style>
:root{
  --page-bg:#03528c;
  --card-bg:#ffffff;
  --brand-blue:#1272bf;
  --deep-blue:#0b2a78;
  --brand-green:#0fa88f;
  --text-grey:#5a5a5a;
  --text-dark:#1b1b1b;
  --map-grey:#d9dcdf;
}
*{box-sizing:border-box;margin:0;padding:0}
html,body{width:1139px;height:1200px;overflow:hidden}
body{background:var(--page-bg);font-family:"Source Sans 3",Arial,sans-serif;position:relative}
.newsletter{position:absolute;left:285px;top:60px;width:569px;height:1080px;background:var(--card-bg)}
.abs{position:absolute}
.heading-font{font-family:"Exo 2",Arial,sans-serif}

.brand{left:0;width:569px;top:52px;display:flex;justify-content:center;align-items:center;gap:10px}
.brand-mark{width:22px;height:22px;background:var(--brand-blue)}
.brand-name{font-family:"Exo 2",Arial,sans-serif;font-weight:800;font-size:28px;color:var(--brand-blue);letter-spacing:1px}
.top-nav{right:16px;top:24px;font-size:12px;color:var(--brand-green)}
.top-nav a{color:inherit;text-decoration:none}

.tagline-band{left:0;top:99px;width:569px;height:31px;background:var(--brand-blue);color:#fff;text-align:center;font-size:14px;font-weight:700;line-height:31px;letter-spacing:.3px}
.hero{left:0;top:132px;width:569px;height:215px;background:linear-gradient(90deg,#3fa3e6 0%,#2a86d4 35%,#123d9c 62%,var(--deep-blue) 100%)}
.hero-title{right:25px;top:202px;color:#fff;font-size:23px;font-weight:800;line-height:29px;text-align:right;text-shadow:0 1px 2px rgba(0,0,0,.5);letter-spacing:.5px}

.news-flash{left:0;top:349px;width:569px;height:42px}
.news-flash svg{position:absolute;left:0;top:0}
.news-flash-label{left:17px;top:10px;color:#fff;font-size:16px;font-weight:700}
.news-flash-text{left:147px;top:5px;width:415px;color:#fff;font-size:12.5px;line-height:14px}

.section-title{font-size:16px;font-weight:700}
.cover-title{left:18px;top:411px;color:var(--brand-blue)}
.cover-text{left:18px;top:436px;width:296px;font-size:11.5px;line-height:15px;color:var(--text-grey);text-align:justify}
.cover-photo{left:337px;top:436px;width:212px;height:72px;background:linear-gradient(90deg,#b9bcc0,#e4e6e8 45%,#8d929a 75%,#c8cacd)}

.ribbon{height:31px}
.ribbon svg{position:absolute;left:0;top:0}
.ribbon span{position:absolute;top:7px;color:#fff;font-size:14px;font-weight:700;white-space:nowrap}
.tips-ribbon{left:0;top:517px;width:262px}
.dates-ribbon{left:0;top:764px;width:262px}
.spot-ribbon{left:316px;top:764px;width:253px}

.tips-list{left:25px;top:557px;width:290px;list-style:none}
.tips-list li{display:flex;gap:9px;font-size:11.5px;line-height:14px;color:var(--text-dark);margin-bottom:11.5px}
.tips-list svg{flex:none;margin-top:3px}

.ceo{left:337px;top:528px;width:215px}
.ceo-title{color:var(--brand-green)}
.sub-heading{color:var(--brand-green);font-size:11.5px;font-weight:600}
.ceo .sub-heading{margin-top:6px}
.ceo p{font-size:11.5px;line-height:15px;color:var(--text-dark);margin-top:7px}
.ceo p + p{margin-top:15px}
.ceo .signature{color:var(--brand-blue);font-weight:600;margin-top:14px}

.events{left:32px;top:806px;width:260px;list-style:none}
.events li{display:flex;gap:8px;margin-bottom:14px}
.events svg{flex:none;margin-top:3px}
.event-date{color:var(--brand-blue);font-size:11.5px;font-weight:600}
.events p{font-size:11.5px;line-height:15px;color:var(--text-dark)}

.county-map{left:330px;top:808px;width:225px;height:122px;background:radial-gradient(ellipse at 50% 50%,var(--map-grey) 0%,#eceef0 60%,#ffffff 100%)}

.footer{left:0;top:1001px;width:569px;text-align:center;font-size:11px;line-height:17px;color:var(--brand-green)}
.footer a{color:inherit}
</style>
</head>
<body>
<div class="newsletter">
  <div class="abs brand"><span class="brand-mark"></span><span class="brand-name">Vaultrix</span></div>
  <nav class="abs top-nav"><a href="#">Home</a> I &nbsp;<a href="#">About Us</a> &nbsp;I <a href="#">Contact Us</a></nav>

  <div class="abs tagline-band heading-font">YOUR LOCAL COMPLETE STORAGE EXPERT</div>

  <div class="abs hero" role="img" aria-label="Photo of open blue storage lockers"></div>
  <div class="abs hero-title heading-font">SECURE DOCUMENT<br>STORAGE &amp; LIFETIME</div>

  <div class="abs news-flash">
    <svg width="569" height="42" viewBox="0 0 569 42">
      <rect x="0" y="0" width="569" height="42" fill="#1272bf"/>
      <polygon points="0,0 118,0 132,21 118,42 0,42" fill="#0fa88f"/>
      <polyline points="120,0 134,21 120,42" fill="none" stroke="#ffffff" stroke-width="2"/>
    </svg>
    <div class="abs news-flash-label heading-font">News Flash</div>
    <div class="abs news-flash-text">consectetur adipiscing elit. Proin leo augue, ornare a pretium in, imperdiet sit amet est. Proin ac elit mauris, ut lacinia eros.</div>
  </div>

  <h2 class="abs section-title heading-font cover-title">Cover Story</h2>
  <p class="abs cover-text">Vaultrix has invested in the latest technologies, security measures and facilities over the years to ensure that your data is stored and managed in the best way and the most suitable environment possible.</p>
  <div class="abs cover-photo" role="img" aria-label="Photo of a secure storage vault room"></div>

  <div class="abs ribbon tips-ribbon">
    <svg width="262" height="31"><polygon points="0,0 248,0 262,15.5 248,31 0,31" fill="#1272bf"/></svg>
    <span class="heading-font" style="left:15px">TIPS AND HELPFUL INFORMATION</span>
  </div>
  <ul class="abs tips-list">
    <li><svg width="14" height="12"><polyline points="1,6 5,11 13,1" fill="none" stroke="#0fa88f" stroke-width="3"/></svg>Nulla tempor lectus a justo vulputate ut rutrum odio porttitor. Pellentesque a consectetur lectus.</li>
    <li><svg width="14" height="12"><polyline points="1,6 5,11 13,1" fill="none" stroke="#0fa88f" stroke-width="3"/></svg>Nulla tempor lectus a justo vulputate ut rutrum odio porttitor. Pellentesque a consectetur lectus.</li>
    <li><svg width="14" height="12"><polyline points="1,6 5,11 13,1" fill="none" stroke="#0fa88f" stroke-width="3"/></svg>Nulla tempor lectus a justo vulputate ut rutrum odio porttitor. Pellentesque a consectetur lectus.</li>
    <li><svg width="14" height="12"><polyline points="1,6 5,11 13,1" fill="none" stroke="#0fa88f" stroke-width="3"/></svg>Nulla tempor lectus a justo vulputate ut rutrum odio porttitor. Pellentesque a consectetur lectus.</li>
    <li><svg width="14" height="12"><polyline points="1,6 5,11 13,1" fill="none" stroke="#0fa88f" stroke-width="3"/></svg>Nulla tempor lectus a justo vulputate ut rutrum odio porttitor. Pellentesque a consectetur lectus.</li>
  </ul>

  <section class="abs ceo">
    <h2 class="section-title heading-font ceo-title">CEO’s Corner</h2>
    <div class="sub-heading">Heading Here</div>
    <p>Nulla tempor lectus a justo vulputate ut rutrum odio porttitor. Pellentesque a consectetur lectus.</p>
    <p>Nulla tempor lectus a justo vulputate ut rutrum odio porttitor. Pellentesque a consectetur lectus.<br>Nulla tempor lectus a justo vulputate ut rutrum odio porttitor.</p>
    <div class="sub-heading signature">Director Name</div>
  </section>

  <div class="abs ribbon dates-ribbon">
    <svg width="262" height="31"><polygon points="0,0 248,0 262,15.5 248,31 0,31" fill="#1272bf"/></svg>
    <span class="heading-font" style="left:20px">IMPORTANT DATES AND EVENTS</span>
  </div>
  <div class="abs ribbon spot-ribbon">
    <svg width="253" height="31"><polygon points="14,0 253,0 253,31 14,31 0,15.5" fill="#1272bf"/></svg>
    <span class="heading-font" style="left:25px">SPOTLIGHT ON THE COUNTIES</span>
  </div>

  <ul class="abs events">
    <li><svg width="9" height="11"><polyline points="2,1 7,5.5 2,10" fill="none" stroke="#0fa88f" stroke-width="2.5"/></svg>
      <div><div class="event-date">25 May 2014</div><div class="sub-heading">Heading Here</div><p>Nulla tempor lectus a justo vulputate ut rutrum odio porttitor. Pellentesque a consectetur lectus.</p></div></li>
    <li><svg width="9" height="11"><polyline points="2,1 7,5.5 2,10" fill="none" stroke="#0fa88f" stroke-width="2.5"/></svg>
      <div><div class="event-date">25 May 2014</div><div class="sub-heading">Heading Here</div><p>Nulla tempor lectus a justo vulputate ut rutrum odio porttitor. Pellentesque a consectetur lectus.</p></div></li>
  </ul>

  <div class="abs county-map" role="img" aria-label="Light grey world map with location markers"></div>

  <footer class="abs footer">
    <div><a href="#">Unsubscribe</a> from future marketing emails. &nbsp; <a href="#">View Our Privacy Policy</a> &nbsp; | &nbsp; <a href="#">Forward to a Friend</a></div>
    <div>Vaultrix Storage, 48 Harbor Lane, Suite 210, Riverton, USA</div>
  </footer>
</div>
</body>
</html>
```